Providing Back Office Solutions to Financial Advisors and Attorney Needs a Business Card Design

Need a Business Card Design that speaks to Financial Advisor and Attorneys. Some of the word that come to mind is Clean/Simple & Futuristic.

Industry/Entity Type

Business

```html
<!DOCTYPE html>
<html lang="en">
<head>
<meta charset="utf-8">
<title>Alderwick Back Office Solutions – Business Card</title>
<link rel="stylesheet" href="https://fonts.googleapis.com/css2?family=Source+Sans+3:wght@400;500;600&display=swap">
<style>
  :root {
    --backdrop: #ece9e4;
    --kraft-light: #cdb088;
    --kraft: #c2a378;
    --kraft-dark: #b39367;
    --ink: #1c1a17;
  }
  * { margin: 0; padding: 0; box-sizing: border-box; }
  html, body { width: 1200px; height: 900px; overflow: hidden; }
  body {
    position: relative;
    background: var(--backdrop);
    font-family: "Source Sans 3", Arial, sans-serif;
    color: var(--ink);
  }
  .card {
    position: absolute;
    width: 556px;
    height: 342px;
    background: radial-gradient(ellipse at 45% 35%, var(--kraft-light), var(--kraft) 55%, var(--kraft-dark));
    box-shadow: 0 6px 18px rgba(0,0,0,0.18);
  }
  .card--front { left: 238px; top: 62px; }
  .card--back  { left: 458px; top: 518px; }

  .contact {
    position: absolute;
    left: 0; right: 0; top: 74px;
    text-align: center;
    line-height: 1;
  }
  .contact__name { font-size: 21px; font-weight: 500; letter-spacing: 0.3px; }
  .contact__role { font-size: 15px; margin-top: 6px; }
  .contact__rule {
    width: 155px; height: 1px; background: var(--ink);
    margin: 15px auto 0;
  }
  .contact__details { font-size: 15.5px; margin-top: 14px; }
  .contact__details p { height: 20.5px; }
  .contact__details b { font-weight: 600; }
  .contact__web { font-weight: 600; }
  .contact__address { font-size: 15.5px; margin-top: 15px; }
  .contact__address p { height: 21px; }

  .brand {
    position: absolute;
    left: 0; right: 0; top: 0; bottom: 0;
    display: flex; align-items: center; justify-content: center;
    gap: 16px;
  }
  .brand__square { width: 22px; height: 22px; background: var(--ink); }
  .brand__name {
    font-size: 30px; font-weight: 500; letter-spacing: 0.5px;
    text-transform: uppercase; line-height: 1.15;
  }
</style>
</head>
<body>
  <section class="card card--front">
    <div class="contact">
      <h1 class="contact__name">DANIEL HARPER</h1>
      <p class="contact__role">Managing Director</p>
      <div class="contact__rule"></div>
      <div class="contact__details">
        <p><b>P:</b> 055-987 654 321</p>
        <p><b>E:</b> hello@alderwick.com</p>
        <p class="contact__web">www.alderwick.com</p>
      </div>
      <div class="contact__rule"></div>
      <div class="contact__address">
        <p>48210, Linden Court Road</p>
        <p>Northland, 482107.</p>
      </div>
    </div>
  </section>

  <section class="card card--back">
    <div class="brand">
      <span class="brand__square"></span>
      <span class="brand__name">Alderwick<br>Back Office Solutions</span>
    </div>
  </section>
</body>
</html>
```